Design an App Mockup for a Restaurant discount lottery system

Updated brief:

Choose between these 2:
1- The user picks from 30 different envelopes numbered 1 - 30. The one the user selected should come to the front of the app mockup, and alert a user that he has won a free entree at a restaurant.

2- The user spins a wheel similar to ribbon riches hour, the one he lands on gives alerts the user that he has won a free entree at a restaurant.

```html
<!DOCTYPE html>
<html lang="en">
<head>
<meta charset="utf-8">
<title>Restaurant Discount Lottery – App Screens</title>
<link rel="stylesheet" href="https://fonts.googleapis.com/css2?family=Arimo:wght@400;700&display=swap">
<style>
  :root {
    --page-bg: #f2e6cd;
    --screen-top: #2473a6;
    --screen-mid: #1f6f9a;
    --screen-bottom: #2c3d8c;
    --win-mid: #2a9aa6;
    --white: #ffffff;
    --navy-text: #14306b;
    --status-light: #ffffff;
    --status-peach: #f9dcc0;
    --accent-teal: #4fb4c6;
    --ring-orange: #ef5f1c;
    --spin-red: #d8261f;
    --ticket-light: #e3e9ec;
    --ticket-shade: #b9c9cf;
  }
  * { box-sizing: border-box; margin: 0; padding: 0; }
  html, body {
    width: 1200px; height: 1200px; overflow: hidden;
    background: var(--page-bg);
    font-family: "Arimo", Arial, sans-serif;
  }
  .canvas { position: relative; width: 1200px; height: 1200px; }
  .screen {
    position: absolute; top: 207px; width: 349px; height: 624px;
    overflow: hidden; color: var(--white);
    background: linear-gradient(180deg, var(--screen-top) 0%, var(--screen-mid) 45%, var(--screen-bottom) 100%);
  }
  .screen--spin { left: 235px; }
  .screen--prize {
    left: 680px;
    background: linear-gradient(180deg, var(--screen-top) 0%, var(--win-mid) 50%, var(--screen-bottom) 100%);
  }
  .status-bar {
    position: relative; z-index: 2;
    height: 23px; display: flex; align-items: center; justify-content: space-between;
    padding: 0 8px; background: var(--status-light); color: #111;
    font-weight: 700; font-size: 15px;
  }
  .screen--prize .status-bar { background: var(--status-peach); }
  .carrier { display: flex; align-items: flex-end; gap: 3px; }
  .signal { display: flex; align-items: flex-end; gap: 1px; height: 10px; }
  .signal span { width: 2px; background: #111; }
  .battery { width: 21px; height: 10px; border: 2px solid #111; border-radius: 2px; position: relative; padding: 1px; }
  .battery::before { content: ""; display: block; height: 100%; background: #111; }
  .battery::after { content: ""; position: absolute; right: -4px; top: 2px; width: 2px; height: 3px; background: #111; }
  .restaurant-name {
    position: absolute; left: 23px; top: 51px; width: 306px; height: 33px;
    background: var(--white); border-radius: 6px; color: var(--navy-text);
    font-weight: 700; font-size: 18px; display: flex; align-items: center; justify-content: center;
  }
  .headline {
    position: absolute; left: 0; width: 100%; text-align: center; font-weight: 700; line-height: 1;
  }
  .headline--luck { top: 146px; font-size: 25px; }
  .headline--congrats { top: 123px; font-size: 25px; }
  .you-won { position: absolute; top: 180px; width: 100%; text-align: center; font-weight: 700; font-size: 17px; line-height: 1; }
  .wheel { position: absolute; left: 0; top: 0; }
  .website-link {
    position: absolute; left: 0; width: 100%; text-align: center; line-height: 1;
    font-size: 19px; color: var(--white); text-decoration: underline;
  }
  .screen--spin .website-link { top: 578px; }
  .screen--prize .website-link { top: 590px; }
  .ticket-art {
    position: absolute; left: 9px; top: 237px; width: 324px; height: 170px;
    border-radius: 8px;
    background: linear-gradient(170deg, var(--ticket-light) 0%, var(--ticket-shade) 100%);
    opacity: 0.9;
  }
  .instructions {
    position: absolute; top: 470px; width: 100%; text-align: center;
    font-weight: 700; font-size: 15px; line-height: 1.3;
  }
</style>
</head>
<body>
<main class="canvas">

  <section class="screen screen--spin">
    <div class="status-bar">
      <div class="carrier">
        <div class="signal"><span style="height:3px"></span><span style="height:5px"></span><span style="height:7px"></span><span style="height:8px"></span><span style="height:10px"></span></div>
        CARRIER
      </div>
      <div class="battery"></div>
    </div>
    <div class="restaurant-name">Restaurant name</div>
    <h1 class="headline headline--luck">TRY YOUR LUCK!</h1>

    <svg class="wheel" width="349" height="624" viewBox="0 0 349 624" aria-label="Prize wheel">
      <rect x="245" y="180" width="94" height="73" rx="10" fill="var(--accent-teal)" opacity="0.3" role="img" aria-label="Decorative arrows pointing right"/>
      <rect x="9" y="453" width="90" height="80" rx="10" fill="var(--accent-teal)" opacity="0.3" role="img" aria-label="Decorative arrows pointing left"/>
      <g class="segments" font-family="Arimo, Arial, sans-serif" font-weight="700" text-anchor="middle" fill="var(--white)" font-size="18">
        <g><circle cx="172" cy="244" r="41" fill="#fff"/><circle cx="172" cy="244" r="35" fill="#d9312b"/><text x="172" y="250">sorry</text></g>
        <g><circle cx="251" cy="277" r="41" fill="#fff"/><circle cx="251" cy="277" r="35" fill="#3f3f42"/><text x="251" y="283">50%</text></g>
        <g><circle cx="284" cy="356" r="41" fill="#fff"/><circle cx="284" cy="356" r="35" fill="#3fc1b3"/><text x="284" y="362">sorry</text></g>
        <g><circle cx="251" cy="435" r="41" fill="#fff"/><circle cx="251" cy="435" r="35" fill="#7cc22e"/><text x="251" y="441">75%</text></g>
        <g><circle cx="172" cy="468" r="41" fill="#fff"/><circle cx="172" cy="468" r="35" fill="#4a4a4d"/><text x="172" y="474">sorry</text></g>
        <g><circle cx="93" cy="435" r="41" fill="#fff"/><circle cx="93" cy="435" r="35" fill="#f5a623"/><text x="93" y="441">free!!!</text></g>
        <g><circle cx="60" cy="356" r="41" fill="#fff"/><circle cx="60" cy="356" r="35" fill="#ef6a1f"/><text x="60" y="362">sorry</text></g>
        <g><circle cx="93" cy="277" r="41" fill="#fff"/><circle cx="93" cy="277" r="35" fill="#2fa84f"/><text x="93" y="283">20%</text></g>
      </g>
      <g class="spin-button" font-family="Arimo, Arial, sans-serif" text-anchor="middle">
        <path d="M158 432 h28 l-14 17 z" fill="var(--ring-orange)"/>
        <circle cx="172" cy="356" r="80" fill="var(--ring-orange)"/>
        <circle cx="172" cy="356" r="66" fill="#fff"/>
        <text x="172" y="334" font-size="17" font-weight="700" fill="#111">How much</text>
        <text x="172" y="357" font-size="15" fill="#111">will it cost you</text>
        <text x="172" y="377" font-size="15" fill="#111">dinner?</text>
        <text x="172" y="398" font-size="15" font-weight="700" fill="var(--spin-red)">SPIN!!!</text>
        <line x1="147" y1="401" x2="197" y2="401" stroke="var(--spin-red)" stroke-width="2"/>
      </g>
    </svg>

    <a class="website-link">go to the website</a>
  </section>

  <section class="screen screen--prize">
    <div class="status-bar">
      <div class="carrier">
        <div class="signal"><span style="height:3px"></span><span style="height:5px"></span><span style="height:7px"></span><span style="height:8px"></span><span style="height:10px"></span></div>
        CARRIER
      </div>
      <div class="battery"></div>
    </div>
    <div class="restaurant-name">Restaurant name</div>
    <h1 class="headline headline--congrats">Congratulations!</h1>
    <p class="you-won">You won:</p>

    <div class="ticket-art" role="img" aria-label="Lucky ticket illustration reading: lucky TICKET, 75% discount, with serial number"></div>

    <p class="instructions">Show the code to the waiter<br>and get your prize</p>
    <a class="website-link">go to the website</a>
  </section>

</main>
</body>
</html>
```